A start-up named "Corvath Therapeutics" - needs a new PowerPoint design

We need a new PowerPoint Design for an early-stage start-up named "Corvath Therapeutics" seeking to disrupt the current approach towards drug discovery within aging disorders.

We would like to build on Corvath's legacy, the founder of the modern science of genetics, by employing a multidisciplinary approach, experimenting, and providing elderly patients the attention they deserve.

We have selected the suffix "therapeutics" intentionally as it stands for (a medicine) the treatment of disease; the science of healing. Alzheimer’s treatment is a huge, urgent, unmet need:
- Shift from a disease-management system to a preventive medicine system
- Focus on increasing the health span, not only the life span

Target Market(s)

Pharma/ Biotech Executives Medical Institutions Healthcare professionals (MDs, nurses, payors, pharmacists, etc.) Patients

Industry/Entity Type

Healthcare

Other font styles liked:
• Celias

Colors
0054AA
0677BA
7BADD7
CADEEF
E8F1F8
E54698
E96AAD
F1A4CE
F9D9EA
FCEFF6
A7469A
B969AE
D3A5CF
EDDBEB
F8F0F9
6B429C
8869AF
B7A5CE
E3DAEB
F3F0F8

Requirements
Must have
• - differentiate from other companies named after Corvath - differentiate from other Pharma/ Biotech companies
Nice to have
• simplicity/ minimalist logo vivid colors gradient 3D Life-Sciences inspired Simple geometry Balance
Should not have
• mascot/ emblem watermark logo animated ink style nature-inspired inventive typography artistic chaos

```html
<!DOCTYPE html>
<html lang="en">
<head>
<meta charset="utf-8">
<title>Corvath Therapeutics – Presentation Template</title>
<link href="https://fonts.googleapis.com/css2?family=Outfit:wght@300;400;500;600;700&display=swap" rel="stylesheet">
<style>
  :root{
    --cyan:#35bdf0;
    --sky:#3aa8e6;
    --blue:#0677ba;
    --violet:#6b429c;
    --purple:#8a4fa8;
    --plum:#a7469a;
    --magenta:#c0369b;
    --ink:#1d1d2b;
    --grey:#8a8a96;
    --light:#f3f0f8;
    --brand-grad:linear-gradient(90deg,var(--cyan) 0%,#7f79cc 50%,var(--magenta) 100%);
    --brand-grad-d:linear-gradient(135deg,var(--cyan) 0%,#8a7cd0 50%,var(--magenta) 100%);
    --brand-grad-v:linear-gradient(180deg,var(--cyan) 0%,#8061b8 55%,var(--plum) 100%);
  }
  *{box-sizing:border-box;margin:0;padding:0}
  html,body{width:1200px;height:2194px;overflow:hidden;background:#fff}
  body{position:relative;font-family:"Outfit",sans-serif;color:var(--ink)}
  .slide{position:absolute;width:504px;height:284px;overflow:hidden;background:#fff;box-shadow:0 6px 18px rgba(40,30,70,.22)}
  .abs{position:absolute}
  .photo{position:absolute;overflow:hidden}
  .logo{position:absolute;display:flex;align-items:center;gap:4px;font-weight:500;color:var(--violet);font-size:7px;white-space:nowrap}
  .logo-mark{width:9px;height:9px;background:var(--violet)}
  .logo.white{color:#fff}.logo.white .logo-mark{background:#fff}
  .title{position:absolute;font-size:21px;line-height:1.12;font-weight:300;color:var(--ink)}
  .title b{font-weight:700}
  .body{font-size:4.6px;line-height:1.6;color:var(--grey);text-align:justify}
  .body.white{color:rgba(255,255,255,.9)}
  .foot{position:absolute;left:38px;bottom:11px;font-size:4.6px;color:var(--grey)}
  .foot.white{color:#fff}
  .page{position:absolute;right:30px;bottom:11px;font-size:4.6px;color:var(--cyan)}
  .page.white{color:#fff}
  .card{position:absolute;background:#fff;border-radius:8px;box-shadow:0 4px 12px rgba(40,30,70,.18)}
  .caption{font-size:7px;color:#fff;text-align:center}
  .item-title{font-size:7.5px;color:var(--ink)}
  .num{font-size:15px;font-weight:300;color:var(--cyan)}
  .num small{font-size:7px}
</style>
</head>
<body>

<!-- Row 1 : cover slides -->
<section class="slide" style="left:70px;top:34px;background:var(--brand-grad-d)">
  <div class="photo" role="img" aria-label="Photo of an elderly couple embracing by the sea, tinted with the brand gradient" style="left:190px;top:0;width:314px;height:284px;background:linear-gradient(90deg,rgba(255,255,255,0) 0%,rgba(230,210,235,.25) 40%,rgba(190,150,200,.3) 100%)"></div>
  <svg class="abs" style="left:0;bottom:0" width="504" height="80" viewBox="0 0 504 80">
    <path d="M0 80 C150 40 330 30 504 58 L504 80Z" fill="rgba(192,54,155,.55)"/>
    <path d="M0 78 C160 42 330 36 504 52" fill="none" stroke="rgba(255,255,255,.7)" stroke-width="1.5"/>
  </svg>
  <div class="logo white" style="left:37px;top:108px;font-size:20px;gap:8px"><span class="logo-mark" style="width:22px;height:22px"></span>Corvath Therapeutics</div>
  <p class="abs" style="left:40px;top:156px;font-size:11.5px;font-weight:300;color:#fff;line-height:1.25">Focus on increasing the health<br>span, not only the life span</p>
</section>

<section class="slide" style="left:624px;top:34px">
  <div class="photo" role="img" aria-label="Photo of an elderly couple embracing outdoors" style="left:170px;top:0;width:334px;height:284px;background:linear-gradient(90deg,#fff 0%,#e6e9ee 25%,#a7b0b3 55%,#6f7a70 80%,#58624f 100%)"></div>
  <div class="logo" style="left:38px;top:108px;font-size:20px;gap:8px"><span class="logo-mark" style="width:22px;height:22px"></span>Corvath Therapeutics</div>
  <p class="abs" style="left:40px;top:156px;font-size:11.5px;font-weight:300;color:var(--purple);line-height:1.25">Focus on increasing the health<br>span, not only the life span</p>
</section>

<!-- Row 2 -->
<section class="slide" style="left:70px;top:341px">
  <div class="abs" style="left:0;top:0;width:252px;height:284px;background:var(--brand-grad-v)"></div>
  <div class="photo" role="img" aria-label="Photo of a senior artist painting in a studio" style="left:25px;top:36px;width:355px;height:212px;border-radius:10px;background:linear-gradient(135deg,#6b6e5c,#a99b84 40%,#8a5a40 70%,#4d4a45)"></div>
  <div class="card" style="left:287px;top:55px;width:189px;height:173px;padding:18px 22px">
    <div style="font-size:21px;font-weight:300">About <b style="font-weight:700">Us</b></div>
    <p style="font-size:8px;color:var(--cyan);margin:6px 0 8px;line-height:1.3">You could include a<br>subtitle here</p>
    <p class="body">Lorem Ipsum is simply dummy text of the printing and typesetting industry. Lorem Ipsum has been the industry's standard dummy text ever since the 1500s, when an unknown printer took a galley of type and scrambled it to make a type specimen book. It has survived not only five centuries, but also the leap into electronic typesetting, remaining essentially unchanged.</p>
  </div>
  <div class="logo" style="left:404px;top:20px"><span class="logo-mark"></span>Corvath Therapeutics</div>
  <div class="foot white">© 2021 Corvath Therapeutics. All rights reserved</div>
  <div class="page">Page 5</div>
</section>

<section class="slide" style="left:624px;top:341px">
  <svg class="abs" style="left:0;top:0" width="504" height="284" viewBox="0 0 504 284">
    <defs><linearGradient id="g4" x1="0" y1="0" x2="1" y2="1"><stop offset="0" stop-color="#35bdf0"/><stop offset=".55" stop-color="#7d67c0"/><stop offset="1" stop-color="#a7469a"/></linearGradient></defs>
    <path d="M290 0 L504 0 L504 284 L350 284 C410 250 440 200 420 120 C400 50 340 20 290 0Z" fill="url(#g4)"/>
  </svg>
  <div class="logo" style="left:40px;top:20px"><span class="logo-mark"></span>Corvath Therapeutics</div>
  <div class="title" style="left:44px;top:66px">Two images<br><b>plus text</b></div>
  <p class="body abs" style="left:44px;top:130px;width:140px">Lorem Ipsum is simply dummy text of the printing and typesetting industry. Lorem Ipsum has been the industry's standard dummy text ever since the 1500s, when an unknown printer took a galley of type and scrambled it to make a type specimen book. It has survived not only five centuries, but also the leap into electronic typesetting, remaining essentially unchanged. It was popularized in the 1960s with the release of Letraset sheets containing Lorem Ipsum passages, and more recently with desktop.</p>
  <div class="card" style="left:198px;top:56px;width:274px;height:189px"></div>
  <div class="photo" role="img" aria-label="Photo of laboratory pipette and sample dish" style="left:215px;top:55px;width:117px;height:125px;border-radius:8px 8px 0 0;background:linear-gradient(160deg,#e8eef2,#c8d2d8 50%,#d98a86)"></div>
  <div class="abs caption" style="left:215px;top:180px;width:117px;height:20px;line-height:20px;background:var(--sky);border-radius:0 0 8px 8px">Image title one</div>
  <div class="photo" role="img" aria-label="Photo of a gloved hand using a pipette over a well plate" style="left:342px;top:55px;width:117px;height:125px;border-radius:8px 8px 0 0;background:linear-gradient(160deg,#3c3f4a,#7f8391 50%,#2d7fd6)"></div>
  <div class="abs caption" style="left:342px;top:180px;width:117px;height:20px;line-height:20px;background:var(--magenta);border-radius:0 0 8px 8px">Image title two</div>
  <p class="body abs" style="left:215px;top:214px;width:244px">Lorem Ipsum is simply dummy text of the printing and typesetting industry. Lorem Ipsum has been the industry's standard dummy text ever since the 1500s, when an unknown printer took a galley of type and scrambled it to make a type specimen.</p>
  <div class="foot">© 2021 Corvath Therapeutics. All rights reserved</div>
  <div class="page white">Page 6</div>
</section>

<!-- Row 3 -->
<section class="slide" style="left:70px;top:649px">
  <div class="logo" style="left:32px;top:20px"><span class="logo-mark"></span>Corvath Therapeutics</div>
  <div class="photo" role="img" aria-label="Abstract fluid paint texture in orange and teal" style="left:32px;top:68px;width:440px;height:216px;border-radius:8px 0 0 0;background:linear-gradient(180deg,#f0a35c 0%,#e9b080 25%,#3c9ec2 60%,#1f6e96 100%)"></div>
  <div class="abs" style="left:103px;top:40px;width:384px;height:205px;border-radius:8px;background:var(--brand-grad)"></div>
  <div class="abs" style="left:123px;top:73px;font-size:21px;font-weight:300;color:#fff;line-height:1.15">Two images<br>plus text</div>
  <p class="body white abs" style="left:123px;top:137px;width:115px">Lorem Ipsum is simply dummy text of the printing and typesetting industry. Lorem Ipsum has been the industry's standard dummy text ever since the 1500s, when an unknown printer took a galley of type and scrambled it to make a type specimen book</p>
  <div class="card" style="left:261px;top:68px;width:98px;height:148px;border-radius:3px"></div>
  <div class="photo" role="img" aria-label="Photo of a senior man reading a newspaper" style="left:261px;top:68px;width:98px;height:68px;border-radius:3px 3px 0 0;background:linear-gradient(135deg,#8b8f8a,#d8d6cc 60%,#b8b4a8)"></div>
  <div class="abs" style="left:269px;top:145px;font-size:7.5px;color:var(--cyan)">Image title one</div>
  <p class="body abs" style="left:269px;top:158px;width:82px;text-align:left">Lorem Ipsum is simply dummy text of the printing and typesetting industry.</p>
  <div class="card" style="left:367px;top:68px;width:98px;height:148px;border-radius:3px"></div>
  <div class="photo" role="img" aria-label="Photo of a senior artist painting" style="left:367px;top:68px;width:98px;height:68px;border-radius:3px 3px 0 0;background:linear-gradient(135deg,#6b6e5c,#a99b84 50%,#8a5a40)"></div>
  <div class="abs" style="left:375px;top:145px;font-size:7.5px;color:var(--purple)">Image title two</div>
  <p class="body abs" style="left:375px;top:158px;width:82px;text-align:left">Lorem Ipsum is simply dummy text of the printing and typesetting industry.</p>
  <div class="page" style="right:18px;color:#fff">Page 7</div>
</section>

<section class="slide" style="left:624px;top:649px">
  <div class="logo" style="left:40px;top:20px"><span class="logo-mark"></span>Corvath Therapeutics</div>
  <div class="title" style="left:44px;top:66px">Four images<br><b>plus text</b></div>
  <p class="body abs" style="left:44px;top:130px;width:140px">Lorem Ipsum is simply dummy text of the printing and typesetting industry. Lorem Ipsum has been the industry's standard dummy text ever since the 1500s, when an unknown printer took a galley of type and scrambled it to make a type specimen book. It has survived not only five centuries, but also the leap into electronic typesetting, remaining essentially unchanged. It was popularized in the 1960s with the release of Letraset sheets containing Lorem Ipsum passages, and more recently with desktop.</p>
  <div class="abs" style="left:274px;top:72px;width:30px;height:30px;border-radius:5px;background:var(--brand-grad-v)"></div>
  <div class="abs" style="left:224px;top:145px;width:40px;height:40px;border-radius:6px;background:var(--brand-grad-v)"></div>
  <div class="abs" style="left:335px;top:122px;width:70px;height:74px;border-radius:8px;background:var(--brand-grad-v)"></div>
  <div class="photo" role="img" aria-label="Photo of a senior man reading" style="left:294px;top:36px;width:56px;height:56px;border-radius:10px;background:linear-gradient(135deg,#8b8f8a,#d8d6cc 60%,#b8b4a8);box-shadow:0 4px 10px rgba(0,0,0,.2)"></div>
  <div class="photo" role="img" aria-label="Photo of a senior artist painting" style="left:365px;top:36px;width:120px;height:117px;border-radius:14px;background:linear-gradient(135deg,#6b6e5c,#a99b84 45%,#8a5a40 75%,#4d4a45);box-shadow:0 4px 10px rgba(0,0,0,.2)"></div>
  <div class="photo" role="img" aria-label="Photo of laboratory sample dish" style="left:213px;top:94px;width:85px;height:85px;border-radius:12px;background:linear-gradient(160deg,#e8eef2,#c8d2d8 50%,#d98a86);box-shadow:0 4px 10px rgba(0,0,0,.2)"></div>
  <div class="photo" role="img" aria-label="Photo of a gloved hand pipetting into a well plate" style="left:268px;top:158px;width:100px;height:100px;border-radius:14px;background:linear-gradient(160deg,#3c3f4a,#8a8e9a 50%,#2d7fd6);box-shadow:0 4px 10px rgba(0,0,0,.2)"></div>
  <div class="foot">© 2021 Corvath Therapeutics. All rights reserved</div>
  <div class="page">Page 8</div>
</section>

<!-- Row 4 -->
<section class="slide" style="left:70px;top:956px">
  <div class="abs" style="left:0;top:233px;width:504px;height:51px;background:var(--brand-grad)"></div>
  <div class="abs" style="left:460px;top:142px;width:44px;height:142px;background:linear-gradient(180deg,#8a4fa8,#7a3f98)"></div>
  <div class="logo" style="left:32px;top:20px"><span class="logo-mark"></span>Corvath Therapeutics</div>
  <div class="title" style="left:30px;top:63px;font-size:20px">Bullet text and<br><b>image slide</b></div>
  <svg class="abs" style="left:28px;top:132px" width="26" height="22" viewBox="0 0 26 22"><g fill="none" stroke="var(--magenta)" stroke-width="1.6"><path d="M2 20h22M4 7h18M5 7v13M10 7v13M16 7v13M21 7v13M13 1l10 6H3z"/></g></svg>
  <div class="abs item-title" style="left:65px;top:130px">Your title text here</div>
  <p class="body abs" style="left:65px;top:142px;width:175px">Lorem Ipsum is simply dummy text of the printing and typesetting industry. Lorem Ipsum has been the industry's standard dummy text ever since the 1500s, when</p>
  <svg class="abs" style="left:32px;top:184px" width="20" height="26" viewBox="0 0 20 26"><g fill="none" stroke="var(--cyan)" stroke-width="1.6"><path d="M7 2h6M9 2v9L3 22h14L11 11V2M2 24h16"/></g></svg>
  <div class="abs item-title" style="left:65px;top:184px">Your title text here</div>
  <p class="body abs" style="left:65px;top:196px;width:175px">Lorem Ipsum is simply dummy text of the printing and typesetting industry. Lorem Ipsum has been the industry's standard dummy text ever since the 1500s, when</p>
  <div class="photo" role="img" aria-label="Photo of a hand holding a culture plate with purple samples" style="left:261px;top:49px;width:195px;height:186px;border-radius:8px;background:linear-gradient(135deg,#3b56c9,#5f4ad0 40%,#2a2e8c 75%,#1c2050)"></div>
  <div class="foot white" style="left:38px">© 2021 Corvath Therapeutics. All rights reserved</div>
  <div class="page white">Page 9</div>
</section>

<section class="slide" style="left:624px;top:956px">
  <div class="logo" style="left:33px;top:20px"><span class="logo-mark"></span>Corvath Therapeutics</div>
  <div class="title" style="left:36px;top:45px;font-size:20px">Images <b>plus text</b></div>
  <p class="body abs" style="left:36px;top:78px;width:192px">Lorem Ipsum is simply dummy text of the printing and typesetting industry. Lorem Ipsum has been the industry's standard dummy text ever since the 1500s, when an unknown printer took a galley of type and scrambled it to make a type specimen book. It has survived not only five centuries, but also the leap into electronic typesetting, remaining essentially.</p>
  <div class="abs" style="left:252px;top:35px;width:102px;height:108px;background:linear-gradient(160deg,var(--cyan),#8a4fa8);padding:12px 10px;color:#fff">
    <div style="font-size:10px;font-weight:700">“</div>
    <div style="font-size:8px;font-weight:700;line-height:1.15">Focus on increasing the health span, not only the life span</div>
    <div style="font-size:4.6px;margin-top:6px">- by Corvath Therapeutics</div>
  </div>
  <div class="photo" role="img" aria-label="Photo of a senior artist painting, tinted blue and magenta" style="left:358px;top:35px;width:103px;height:108px;background:linear-gradient(180deg,#4aa9cf,#8c6bb0 70%,#a7469a)"></div>
  <div class="abs" style="left:366px;top:98px;width:88px;color:#fff"><div style="font-size:6.5px;font-weight:600">Your title text here</div><p style="font-size:4.4px;line-height:1.5;margin-top:3px">Lorem Ipsum is simply dummy text of the printing and typesetting industry.</p></div>
  <div class="photo" role="img" aria-label="Photo of a smiling senior man, tinted with the brand gradient" style="left:36px;top:148px;width:218px;height:82px;background:linear-gradient(180deg,#d3d0c8 0%,#b895b8 60%,#b7399f 100%)"></div>
  <div class="abs" style="left:46px;top:193px;width:200px;color:#fff"><div style="font-size:6.5px;font-weight:600">Your title text here</div><p style="font-size:4.4px;line-height:1.5;margin-top:3px">Lorem Ipsum is simply dummy text of the printing and typesetting industry. Lorem Ipsum has been the industry's standard dummy text ever since the 1500s</p></div>
  <div class="photo" role="img" aria-label="Photo of an elderly couple, tinted with the brand gradient" style="left:257px;top:148px;width:103px;height:82px;background:linear-gradient(180deg,#6cc3e6 0%,#9a7fbd 60%,#b7399f 100%)"></div>
  <div class="abs" style="left:265px;top:193px;width:88px;color:#fff"><div style="font-size:6.5px;font-weight:600">Your title text here</div><p style="font-size:4.4px;line-height:1.5;margin-top:3px">Lorem Ipsum is simply dummy text of the printing and typesetting industry.</p></div>
  <div class="abs" style="left:358px;top:148px;width:103px;height:108px;background:linear-gradient(180deg,var(--sky),#3d7fcf)"></div>
  <p class="body white abs" style="left:366px;top:157px;width:88px">Lorem Ipsum is simply dummy text of the printing and typesetting industry. Lorem Ipsum has been the industry's standard dummy text ever since the 1500s, when an unknown printer took a galley of type and scrambled it to make a type</p>
  <div class="foot">© 2021 Corvath Therapeutics. All rights reserved</div>
  <div class="page">Page 10</div>
</section>

<!-- Row 5 -->
<section class="slide" style="left:70px;top:1263px">
  <div class="logo" style="left:404px;top:20px"><span class="logo-mark"></span>Corvath Therapeutics</div>
  <div class="abs" style="left:69px;top:58px;width:102px;height:95px;background:var(--brand-grad-v)"></div>
  <div class="abs" style="left:68px;top:185px;width:40px;height:40px;background:var(--cyan)"></div>
  <div class="photo" role="img" aria-label="Photo of a woman doing a yoga stretch" style="left:46px;top:58px;width:91px;height:95px;background:linear-gradient(160deg,#d9dde2,#f08a3a 55%,#3d4f8a);box-shadow:0 4px 10px rgba(0,0,0,.2)"></div>
  <div class="photo" role="img" aria-label="Photo of a man jogging on a forest path" style="left:93px;top:93px;width:132px;height:132px;background:linear-gradient(180deg,#3f7d2c,#6fae3f 50%,#a9a38d);box-shadow:0 4px 10px rgba(0,0,0,.2)"></div>
  <div class="title" style="left:251px;top:52px;font-size:21px">Two images<br><b>text &amp; bullets</b></div>
  <p class="body abs" style="left:251px;top:110px;width:220px">Lorem Ipsum is simply dummy text of the printing and typesetting industry. Lorem Ipsum has been the industry's standard dummy text ever since the 1500s, when an unknown printer took a galley of type and scrambled it to make a type specimen book. It has survived not only five centuries, but also the leap into electronic typesetting.</p>
  <svg class="abs" style="left:251px;top:168px" width="26" height="22" viewBox="0 0 26 22"><g fill="none" stroke="var(--magenta)" stroke-width="1.6"><path d="M2 20h22M4 7h18M5 7v13M10 7v13M16 7v13M21 7v13M13 1l10 6H3z"/></g></svg>
  <div class="abs item-title" style="left:288px;top:165px">Your title text here</div>
  <p class="body abs" style="left:288px;top:177px;width:183px">Lorem Ipsum is simply dummy text of the printing and typesetting industry. Lorem Ipsum has been the industry's</p>
  <svg class="abs" style="left:256px;top:204px" width="20" height="26" viewBox="0 0 20 26"><g fill="none" stroke="var(--cyan)" stroke-width="1.6"><path d="M7 2h6M9 2v9L3 22h14L11 11V2M2 24h16"/></g></svg>
  <div class="abs item-title" style="left:288px;top:204px">Your title text here</div>
  <p class="body abs" style="left:288px;top:216px;width:183px">Lorem Ipsum is simply dummy text of the printing and typesetting industry. Lorem Ipsum has been the industry's</p>
  <div class="page">Page 11</div>
</section>

<section class="slide" style="left:624px;top:1263px">
  <div class="abs" style="left:326px;top:0;width:178px;height:284px;background:var(--brand-grad-v)"></div>
  <div class="logo white" style="left:405px;top:20px"><span class="logo-mark"></span>Corvath Therapeutics</div>
  <div class="photo" role="img" aria-label="Photo of a group exercise class stretching outdoors" style="left:243px;top:60px;width:172px;height:160px;border-radius:6px;background:linear-gradient(160deg,#a8b4c0,#d9c3a8 40%,#f08a3a 60%,#4f5a8a);box-shadow:0 4px 12px rgba(0,0,0,.25)"></div>
  <div class="abs" style="left:48px;top:33px;width:180px"><div class="num">01. <small>Your title text here</small></div><p style="font-size:6.4px;line-height:1.45;color:#444">Lorem Ipsum is simply dummy text of the printing and typesetting industry. Lorem Ipsum has been</p></div>
  <div class="abs" style="left:32px;top:82px;width:202px;height:60px;background:var(--cyan)"></div>
  <div class="abs" style="left:48px;top:89px;width:180px"><div class="num" style="color:#fff">02. <small>Your title text here</small></div><p style="font-size:6.4px;line-height:1.45;color:#fff">Lorem Ipsum is simply dummy text of the printing and typesetting industry. Lorem Ipsum has been</p></div>
  <div class="abs" style="left:48px;top:149px;width:180px"><div class="num">03. <small>Your title text here</small></div><p style="font-size:6.4px;line-height:1.45;color:#444">Lorem Ipsum is simply dummy text of the printing and typesetting industry. Lorem Ipsum has been</p></div>
  <div class="abs" style="left:48px;top:204px;width:180px"><div class="num">04. <small>Your title text here</small></div><p style="font-size:6.4px;line-height:1.45;color:#444">Lorem Ipsum is simply dummy text of the printing and typesetting industry. Lorem Ipsum has been</p></div>
  <div class="foot">© 2021 Corvath Therapeutics. All rights reserved</div>
  <div class="page white">Page 12</div>
</section>

<!-- Row 6 -->
<section class="slide" style="left:70px;top:1570px">
  <svg class="abs" style="left:0;top:0" width="504" height="284" viewBox="0 0 504 284">
    <defs><linearGradient id="g13" x1="0" y1="0" x2="1" y2="0"><stop offset="0" stop-color="#35bdf0"/><stop offset=".5" stop-color="#7d79cc"/><stop offset="1" stop-color="#b7399f"/></linearGradient></defs>
    <path d="M163 284 L163 140 C163 122 175 110 193 110 L504 110 L504 284Z" fill="url(#g13)"/>
  </svg>
  <div class="logo" style="left:32px;top:20px"><span class="logo-mark"></span>Corvath Therapeutics</div>
  <div class="title" style="left:36px;top:60px">Our<br><b>Team</b></div>
  <p class="body abs" style="left:36px;top:127px;width:92px;text-align:left">Lorem Ipsum is simply dummy text of the printing and typesetting industry. Lorem Ipsum has been the industry's standard dummy text ever since the 1500s, when an unknown printer took a galley of type and scrambled it to make a type specimen book. It has survived not only five centuries, but also the leap into electronic typesetting.</p>
  <div class="photo" role="img" aria-label="Photo of a scientist working at a laboratory bench" style="left:202px;top:48px;width:125px;height:105px;border-radius:8px;background:linear-gradient(135deg,#5c6670,#c9d0d4 50%,#7f8a8f);box-shadow:0 4px 10px rgba(0,0,0,.25)"></div>
  <div class="photo" role="img" aria-label="Photo of a scientist at a microscope" style="left:339px;top:48px;width:125px;height:105px;border-radius:8px;background:linear-gradient(135deg,#2c2f33,#6d7378 50%,#b9bec2);box-shadow:0 4px 10px rgba(0,0,0,.25)"></div>
  <div class="abs" style="left:202px;top:163px;width:125px;text-align:center;color:#fff">
    <svg width="30" height="7" viewBox="0 0 30 7"><circle cx="4" cy="3.5" r="3" fill="#fff"/><circle cx="15" cy="3.5" r="3" fill="#fff"/><circle cx="26" cy="3.5" r="3" fill="#fff"/></svg>
    <div style="font-size:9.5px">Dr. Mark Doe</div><div style="font-size:5px;margin-bottom:6px">Founder</div>
    <p style="font-size:4.6px;line-height:1.5">Lorem Ipsum is simply dummy text of the printing and typesetting industry. Lorem Ipsum has been the industry's standard dummy text ever</p>
  </div>
  <div class="abs" style="left:339px;top:163px;width:125px;text-align:center;color:#fff">
    <svg width="30" height="7" viewBox="0 0 30 7"><circle cx="4" cy="3.5" r="3" fill="#fff"/><circle cx="15" cy="3.5" r="3" fill="#fff"/><circle cx="26" cy="3.5" r="3" fill="#fff"/></svg>
    <div style="font-size:9.5px">Dr. John Doe</div><div style="font-size:5px;margin-bottom:6px">Founder</div>
    <p style="font-size:4.6px;line-height:1.5">Lorem Ipsum is simply dummy text of the printing and typesetting industry. Lorem Ipsum has been the industry's standard dummy text ever</p>
  </div>
  <div class="foot">© 2021 Corvath Therapeutics. All rights reserved</div>
  <div class="page white">Page 13</div>
</section>

<section class="slide" style="left:624px;top:1570px">
  <div class="photo" role="img" aria-label="Photo of a woman in an orange top stretching on a mat, tinted blue" style="left:46px;top:38px;width:414px;height:114px;background:linear-gradient(90deg,#2f9fe0 0%,#3aa8e6 45%,#e8894a 70%,#4d82c8 100%)"></div>
  <div class="abs" style="left:62px;top:80px;width:22px;height:22px;background:#fff"></div>
  <div class="abs" style="left:112px;top:78px;font-size:16px;font-weight:300;color:#fff;line-height:1.15">Your title slide<br><b style="font-weight:700">text here</b></div>
  <div class="abs" style="left:49px;top:164px;font-size:8.5px;color:var(--ink)">Your subtitle text and <b>image slide here</b></div>
  <p class="body abs" style="left:49px;top:180px;width:410px;color:#555">It is a long established fact that a reader will be distracted by the readable content of a page when looking at its layout. The point of using Lorem Ipsum is that it has a more-or-less normal distribution of letters, as opposed to using 'Content here, content here', making it look like readable English. Many desktop publishing packages and web page editors now use Lorem Ipsum as their default model text, and a search for 'lorem ipsum' will uncover many web sites still in their infancy. Various versions have evolved over the years, sometimes by accident, sometimes on purpose (injected humour and the like). A wonderful serenity has taken possession of my entire soul, like these sweet mornings of spring which I enjoy with my whole heart. I am alone, and feel the charm of existence in this spot, which was created for the bliss of souls like mine. I am so happy, my dear friend, so absorbed in the exquisite sense of mere tranquil existence, that I neglect my talents.</p>
  <div class="page">Page 14</div>
</section>

<!-- Row 7 -->
<section class="slide" style="left:70px;top:1877px">
  <div class="logo" style="left:32px;top:20px"><span class="logo-mark"></span>Corvath Therapeutics</div>
  <div class="title" style="left:30px;top:66px;font-size:20px">Text and<br><b>image slide</b></div>
  <p class="body abs" style="left:30px;top:137px;width:120px;color:#555">Fact that a reader will be distracted by the readable content of a page when looking at its layout. The point of using Lorem Ipsum is that it has a more-or-less normal distribution of letters, as opposed to using 'Content here, content here', making it look like readable English. Many desktop publishing packages and web page editors now use Lorem Ipsum as their default model text.</p>
  <div class="photo" role="img" aria-label="Photo of a scientist in gloves working in a laboratory" style="left:169px;top:0;width:157px;height:284px;background:linear-gradient(160deg,#c9d2d6,#8fa3a8 45%,#6cc0b0 60%,#3b4447)"></div>
  <p class="body abs" style="left:347px;top:30px;width:126px;color:#555">Lorem Ipsum is simply dummy text of the printing and typesetting industry. Lorem Ipsum has been the industry's standard dummy text ever since the 1500s, when an unknown printer took a galley of type and scrambled it to make a type specimen book. It has survived not only five centuries, but also the leap into electronic typesetting, remaining essentially unchanged. It was popularized in the 1960s with the release of Letraset. It is a long established<br><br>Fact that a reader will be distracted by the readable content of a page when looking at its layout. The point of using Lorem Ipsum is that it has a more-or-less normal distribution of letters, as opposed to using 'Content here, content here', making it look like readable English. Many desktop publishing packages and web page editors now use Lorem Ipsum as their default model text.</p>
  <div class="page">Page 15</div>
</section>

<section class="slide" style="left:624px;top:1877px">
  <div class="logo" style="left:33px;top:20px"><span class="logo-mark"></span>Corvath Therapeutics</div>
  <div class="logo" style="left:404px;top:20px"><span class="logo-mark"></span>Corvath Therapeutics</div>
  <div class="abs" style="left:38px;top:56px;font-size:9.5px;line-height:1.15">Lorem Ipsum is<br><b>dummy title text</b></div>
  <p class="body abs" style="left:36px;top:84px;width:100px;color:#555">Lorem Ipsum is simply dummy text of the printing and typesetting industry. Lorem Ipsum has been the industry's standard dummy text ever since the 1500s, when an unknown printer took a galley of type and scrambled it to make a type specimen book. It has survived not only five centuries, but also the leap into electronic typesetting, remaining essentially unchanged. It was popularized in the 1960s with the release of Letraset</p>
  <div class="abs" style="left:156px;top:86px;width:1.5px;height:130px;background:var(--magenta)"></div>
  <div class="title" style="left:180px;top:54px;font-size:21px">Paragraph <b>Text Slide</b></div>
  <p class="body abs" style="left:180px;top:88px;width:290px;color:#555">Lorem Ipsum is simply dummy text of the printing and typesetting industry. Lorem Ipsum has been the industry's standard dummy text ever since the 1500s, when an unknown printer took a galley of type and scrambled it to make a type specimen book. It has survived not only five centuries, but also the leap into electronic typesetting, remaining essentially unchanged. It was popularized in the 1960s with the release of Letraset sheets containing Lorem Ipsum passages, and more recently with desktop publishing software like Aldus PageMaker including versions of Lorem Ipsum.</p>
  <div class="abs num" style="left:180px;top:183px;font-weight:600;font-size:13px">01.</div>
  <div class="abs" style="left:208px;top:170px;width:90px"><div style="font-size:7.5px;font-weight:600">Your Subtitle Text</div><p class="body" style="margin-top:6px;text-align:left">Lorem Ipsum is simply dummy text of the printing and typesetting industry. Lorem Ipsum has been</p></div>
  <div class="abs num" style="left:346px;top:183px;font-weight:600;font-size:13px;color:var(--magenta)">02.</div>
  <div class="abs" style="left:377px;top:170px;width:90px"><div style="font-size:7.5px;font-weight:600">Your Subtitle Text</div><p class="body" style="margin-top:6px;text-align:left">Lorem Ipsum is simply dummy text of the printing and typesetting industry. Lorem Ipsum has been</p></div>
  <div class="foot" style="left:48px">© 2021 Corvath Therapeutics. All rights reserved</div>
  <div class="abs" style="left:360px;bottom:10px;font-size:7px">16</div>
  <div class="page">Page 16</div>
</section>

</body>
</html>
```